Experienced and Professional Marriage Celebrant

I need a web design for my services as a marriage celebrant in the Sydney area. I want people to have the impression I am a modern and professional marriage celebrant who can tailor a wedding ceremony and execute the ceremony with a high level of care and accommodate and adapt to any style of wedding and personalities of couples. I like a mint and pink and black theme and I am not sure whether to use the professional photos of me, might be too stiff! But would like to see ideas you can come up with. Happy to use other photos you might have

Reason: I have haven't been able to respond as quickly as I would have liked this last week to comments so extending a few days. Thanks

```html
<!DOCTYPE html>
<html lang="en">
<head>
<meta charset="utf-8">
<title>Lena Hartwell Celebrant</title>
<link rel="stylesheet" href="https://fonts.googleapis.com/css2?family=PT+Sans:wght@400&display=swap">
<style>
  :root {
    --pink: #e0629f;
    --pink-light: #f08cbc;
    --pink-stripe-a: #eab3d3;
    --pink-stripe-b: #df9cc3;
    --charcoal: #3a3a3a;
    --charcoal-dark: #2b2b2b;
    --text: #5a5a5a;
    --heading: #4a4a4a;
    --white: #ffffff;
    --rule: #b9b9b9;
    --frame: #cfcfcf;
  }
  * { margin: 0; padding: 0; box-sizing: border-box; }
  html, body { width: 1084px; height: 1200px; overflow: hidden; }
  body {
    position: relative;
    font-family: Arial, Helvetica, sans-serif;
    color: var(--text);
    background: repeating-linear-gradient(90deg, var(--pink-stripe-a) 0 20px, var(--pink-stripe-b) 20px 40px);
  }
  a { text-decoration: none; }
  .top-band {
    position: absolute; left: 0; top: 0; width: 1084px; height: 179px;
    background: radial-gradient(ellipse at 50% 0%, #5a5a5a 0%, var(--charcoal) 45%, var(--charcoal-dark) 100%);
    border-bottom: 1px dashed #8a8a8a;
  }
  .page {
    position: absolute; left: 91px; top: 85px; width: 904px; height: 961px;
    background: var(--white);
    box-shadow: 0 0 18px rgba(0,0,0,.35);
  }
  .main-nav { position: absolute; left: 153px; top: 54px; width: 781px; height: 56px; }
  .main-nav svg { position: absolute; inset: 0; }
  .main-nav a {
    position: absolute; top: 18px; font-family: "PT Sans", sans-serif; font-size: 12.5px;
    color: #555; transform: translateX(-50%);
  }
  .main-nav a.current { color: var(--pink); }
  .site-title {
    position: absolute; left: 0; width: 1084px; top: 147px; text-align: center;
    font-family: "PT Sans", sans-serif; font-weight: 400; font-size: 32px; color: var(--pink);
  }
  .photo { position: absolute; border: 2px solid var(--frame); }
  .hero { left: 152px; top: 228px; width: 782px; height: 297px;
    background: linear-gradient(180deg, #8eaab8 0%, #a9b3a6 35%, #6f5a45 60%, #b58a62 100%); }
  .section-title {
    position: absolute; font-family: "PT Sans", sans-serif; font-size: 17px; color: var(--heading); font-weight: 400;
  }
  .section-title span { color: var(--pink); }
  .body-text { position: absolute; font-size: 11.5px; line-height: 16.3px; color: var(--text); }
  .welcome-text { left: 152px; top: 579px; width: 503px; }
  .read-more {
    position: absolute; left: 152px; top: 681px; width: 114px; height: 32px; border-radius: 6px;
    background: linear-gradient(180deg, var(--pink-light), var(--pink)); border: 1px solid #d2558f;
    color: #fff; font-family: "PT Sans", sans-serif; font-size: 14px; text-align: center; line-height: 30px;
  }
  .rule { position: absolute; height: 0; border-top: 2px dotted var(--rule); }
  .blog-thumb { width: 55px; height: 51px; border-radius: 2px;
    background: linear-gradient(135deg, #d9b49a, #6d5549); }
  .pink-label { position: absolute; font-size: 11.5px; color: var(--pink); }
  .more { position: absolute; font-size: 11px; color: var(--pink); }
  .portrait { position: absolute; width: 87px; height: 87px; border-radius: 50%;
    background: radial-gradient(circle at 50% 45%, #c99a86 0%, #7b5a4f 55%, #2f3a36 100%); }
  .pull-quote { position: absolute; font-style: italic; font-size: 13px; line-height: 16.3px; color: var(--pink); }
  .testimonial { position: absolute; width: 222px; font-size: 11.5px; line-height: 16.3px; text-align: justify; text-indent: 32px; }
  .quote-mark { position: absolute; font-family: Georgia, serif; font-size: 44px; color: #c8c8c8; line-height: 1; }
  .quote-close { font-family: Georgia, serif; font-size: 40px; color: #c8c8c8; line-height: 0; vertical-align: -16px; margin-left: 4px; }
  .byline { position: absolute; font-style: italic; font-size: 11px; color: var(--pink); }
  .honeymoon { left: 707px; top: 799px; width: 227px; height: 119px;
    background: linear-gradient(135deg, #c9b8a6 0%, #8b6a52 45%, #e9e4de 100%); }
  .site-footer { position: absolute; left: 135px; top: 1046px; width: 817px; height: 90px; }
  .site-footer svg { position: absolute; inset: 0; }
  .footer-nav { position: absolute; top: 26px; width: 100%; text-align: center; font-size: 11px; color: #fff; }
  .footer-nav a { color: #fff; margin: 0 13px; }
  .copyright { position: absolute; top: 49px; width: 100%; text-align: center; font-size: 11px; color: #fff; }
</style>
</head>
<body>
  <div class="top-band"></div>
  <div class="page"></div>

  <nav class="main-nav">
    <svg width="781" height="56" viewBox="0 0 781 56">
      <defs><linearGradient id="navFill" x1="0" y1="0" x2="0" y2="1">
        <stop offset="0" stop-color="#ffffff"/><stop offset="1" stop-color="#d6d6d6"/></linearGradient></defs>
      <path d="M4 0 H777 Q781 0 781 4 V34 Q390 60 0 34 V4 Q0 0 4 0 Z" fill="url(#navFill)"/>
    </svg>
    <a href="#" style="left:160px">home</a>
    <a href="#" class="current" style="left:267px">about us</a>
    <a href="#" style="left:379px">services</a>
    <a href="#" style="left:492px">partners</a>
    <a href="#" style="left:609px">contact us</a>
  </nav>

  <h1 class="site-title">Lena Hartwell Celebrant</h1>

  <div class="photo hero" role="img" aria-label="Wedding party walking hand in hand along a beach at sunset"></div>

  <h2 class="section-title" style="left:151px;top:546px">Welcome to <span>Our Company</span></h2>
  <p class="body-text welcome-text">Lorem Ipsum is simply dummy text of the printing and typesetting industry. Lorem Ipsum has been the industry's standard dummy text ever since the 1500s, when an unknown printer took a galley of type and scrambled it to make a type specimen book. It has survived not only five centuries, but also the leap into electronic typesetting, remaining essentially unchanged.</p>
  <a class="read-more" href="#">read more</a>

  <h2 class="section-title" style="left:706px;top:546px">Latest <span>Blogs</span></h2>
  <div class="photo blog-thumb" style="position:absolute;left:707px;top:581px" role="img" aria-label="Portrait of the celebrant"></div>
  <p class="pink-label" style="left:774px;top:579px">Lorem Ipsum is simply</p>
  <p class="body-text" style="left:774px;top:596px;width:160px">Lorem Ipsum is simply dummy text of the printing and</p>
  <a class="more" href="#" style="left:774px;top:631px">more &rarr;</a>
  <div class="photo blog-thumb" style="position:absolute;left:707px;top:663px" role="img" aria-label="Portrait of the celebrant"></div>
  <p class="pink-label" style="left:774px;top:660px">Lorem Ipsum is simply</p>
  <p class="body-text" style="left:774px;top:677px;width:160px">Lorem Ipsum is simply dummy text of the printing and</p>
  <a class="more" href="#" style="left:774px;top:712px">more &rarr;</a>

  <div class="rule" style="left:154px;top:742px;width:496px"></div>
  <div class="rule" style="left:709px;top:742px;width:221px"></div>

  <h2 class="section-title" style="left:150px;top:764px"><span style="color:var(--heading)">Our</span> <span>Testimonials</span></h2>

  <div class="portrait" style="left:151px;top:797px" role="img" aria-label="Portrait of a happy client"></div>
  <p class="pull-quote" style="left:259px;top:801px;width:120px">Lorem Ipsum is simply dummy text of the printing and typesetting ndustry. Lorem Ipsum.</p>
  <span class="quote-mark" style="left:145px;top:888px">&ldquo;</span>
  <p class="body-text testimonial" style="left:151px;top:896px">Lorem Ipsum is simply dummy text of the printing and typesetting industry. Lorem Ipsum has been the industry's standard dummy text ever since the 1500s,<span class="quote-close">&rdquo;</span></p>
  <p class="byline" style="left:151px;top:984px">- Your Name Here</p>

  <div class="portrait" style="left:423px;top:797px" role="img" aria-label="Portrait of a happy client"></div>
  <p class="pull-quote" style="left:535px;top:801px;width:120px">Lorem Ipsum is simply dummy text of the printing and typesetting ndustry. Lorem Ipsum.</p>
  <span class="quote-mark" style="left:420px;top:888px">&ldquo;</span>
  <p class="body-text testimonial" style="left:426px;top:896px">Lorem Ipsum is simply dummy text of the printing and typesetting industry. Lorem Ipsum has been the industry's standard dummy text ever since the 1500s,<span class="quote-close">&rdquo;</span></p>
  <p class="byline" style="left:426px;top:984px">- Your Name Here</p>

  <h2 class="section-title" style="left:706px;top:764px">Honeymoon <span>Destination</span></h2>
  <div class="photo honeymoon" role="img" aria-label="Newlyweds holding hands close up"></div>
  <p class="pink-label" style="left:707px;top:931px">Lorem Ipsum is simply</p>
  <p class="body-text" style="left:707px;top:950px;width:227px">Lorem Ipsum is simply dummy text of the printing and typesetting industry.</p>
  <a class="more" href="#" style="left:707px;top:984px">more &rarr;</a>

  <footer class="site-footer">
    <svg width="817" height="90" viewBox="0 0 817 90">
      <defs>
        <linearGradient id="footFill" x1="0" y1="0" x2="0" y2="1">
          <stop offset="0" stop-color="#2e2e2e"/><stop offset="1" stop-color="#444"/></linearGradient>
        <radialGradient id="footShadow" cx="0.5" cy="0.5" r="0.5">
          <stop offset="0" stop-color="rgba(0,0,0,.35)"/><stop offset="1" stop-color="rgba(0,0,0,0)"/></radialGradient>
      </defs>
      <ellipse cx="408" cy="80" rx="330" ry="10" fill="url(#footShadow)"/>
      <path d="M0 0 H817 V66 Q817 72 811 72 Q408 96 6 72 Q0 72 0 66 Z" fill="url(#footFill)"/>
    </svg>
    <nav class="footer-nav">
      <a href="#">home</a>|<a href="#">about us</a>|<a href="#">services</a>|<a href="#">partners</a>|<a href="#">Contact us</a>
    </nav>
    <p class="copyright">&copy; Copyright 2014. All Rights Reserved.</p>
  </footer>
</body>
</html>
```